Inviting A6 Flyer for Church membership

We need an A6 size flyer for the church. We are looking for something fresh, inviting and impactful. Church new logo and current flyer design attached.
Back text as follows:
We would love to have you join us as our SPECIAL GUEST this Sunday at 10am.
You can find us at Harvest Lantern Family Church, 17-19 Marlow Crest Road
(Behind Brivo), Thornbury Meadow Village,QX4 7LB
For more information or for a chat, please call us on 07700 900418 / 07700 900752 or email church@hlfcuk-mail.test
Target Market(s)
Church
Industry/Entity Type
Church
Colors
Designer to choose colors to be used in the design.
Requirements
Must have
- fresh, inviting and impactful.
- Chruch logo (attached)
Should not have
- Too much going on

```html
<!DOCTYPE html>
<html lang="en">
<head>
<meta charset="utf-8">
<title>Harvest Lantern Family Church – Special Guest Flyer</title>
<link rel="stylesheet" href="https://fonts.googleapis.com/css2?family=Lato:wght@300;400&family=Kaushan+Script&display=swap">
<style>
  :root {
    --page-bg: #e8e8e8;
    --paper: #ffffff;
    --paper-shade: #f2f2f3;
    --sky-warm: #e9dcc0;
    --sky-gold: #f4ecd6;
    --sky-rose: #b9a39a;
    --sky-blue: #6f7f90;
    --floor-navy: #3a3f58;
    --floor-maroon: #6e3f4a;
    --ink: #333333;
    --ink-soft: #444444;
    --address: #7b8b99;
    --script-blue: #2a6fb0;
    --brand-red: #b8312c;
  }
  * { margin: 0; padding: 0; box-sizing: border-box; }
  html, body {
    width: 1200px; height: 1200px; overflow: hidden;
    background: var(--page-bg);
    font-family: "Lato", sans-serif;
  }
  .flyer {
    position: absolute; left: 246px; top: 100px;
    width: 707px; height: 1000px;
    background: var(--paper);
    box-shadow: 0 6px 24px rgba(0,0,0,0.12);
    overflow: hidden;
  }
  .flyer-art { position: absolute; inset: 0; }
  .brand {
    position: absolute; left: 0; right: 0; top: 262px;
    text-align: center;
  }
  .brand-name {
    font-weight: 400; font-size: 19px; letter-spacing: 0.06em;
    color: var(--brand-red); line-height: 1.1; text-transform: uppercase;
  }
  .invite {
    position: absolute; left: 0; right: 0; top: 375px;
    text-align: center; color: var(--ink);
  }
  .invite-line {
    font-weight: 300; font-size: 36px; line-height: 58px;
  }
  .invite-highlight {
    font-family: "Kaushan Script", cursive;
    font-size: 56px; line-height: 56px;
    color: var(--script-blue);
  }
  .invite-time {
    font-weight: 300; font-size: 34px; line-height: 46px;
  }
  .location {
    position: absolute; left: 0; right: 0; top: 620px;
    text-align: center; color: var(--address);
    font-weight: 300; font-size: 18px; line-height: 24px;
    font-style: normal;
  }
  .contact {
    position: absolute; left: 129px; right: 70px; top: 752px;
    color: var(--ink-soft); font-size: 15px; line-height: 21px;
    font-weight: 400;
  }
</style>
</head>
<body>
  <article class="flyer">
    <svg class="flyer-art" viewBox="0 0 707 1000" width="707" height="1000">
      <defs>
        <linearGradient id="skyTone" x1="0" y1="0" x2="1" y2="0.4">
          <stop offset="0" stop-color="var(--sky-rose)"/>
          <stop offset="0.3" stop-color="var(--sky-warm)"/>
          <stop offset="0.55" stop-color="var(--sky-gold)"/>
          <stop offset="0.85" stop-color="#c9c8c0"/>
          <stop offset="1" stop-color="var(--sky-blue)"/>
        </linearGradient>
        <linearGradient id="floorTone" x1="0" y1="0" x2="1" y2="0">
          <stop offset="0" stop-color="var(--floor-navy)"/>
          <stop offset="0.45" stop-color="var(--floor-maroon)"/>
          <stop offset="0.75" stop-color="#7a4b55"/>
          <stop offset="1" stop-color="var(--floor-navy)"/>
        </linearGradient>
        <linearGradient id="paperTone" x1="0" y1="0" x2="0" y2="1">
          <stop offset="0" stop-color="var(--paper)"/>
          <stop offset="1" stop-color="var(--paper-shade)"/>
        </linearGradient>
      </defs>
      <rect x="0" y="0" width="707" height="440" fill="url(#skyTone)" role="img" aria-label="Photo of sunlight breaking through soft clouds"/>
      <rect x="0" y="780" width="707" height="220" fill="url(#floorTone)" role="img" aria-label="Photo of a softly lit church interior in deep tones"/>
      <path d="M0 419 L207 296 L502 296 L707 419 L707 821 L502 875 L201 875 L0 797 Z" fill="url(#paperTone)"/>
      <circle cx="353" cy="249" r="151" fill="var(--paper)"/>
    </svg>

    <header class="brand">
      <p class="brand-name">Harvest Lantern Ministries</p>
    </header>

    <section class="invite">
      <p class="invite-line">We would love to</p>
      <p class="invite-line">have you join us as our</p>
      <p class="invite-highlight">Special Guest</p>
      <p class="invite-time">this Sunday at 10am</p>
    </section>

    <address class="location">
      You can find us at<br>
      Harvest Lantern Family Church, 17-19<br>
      Marlow Crest Road (Behind Brivo),<br>
      Thornbury Meadow Village,QX4 7LB
    </address>

    <p class="contact">
      For more information or for a chat, please call us on 07700
      900418 / 07700 900752 or email church@hlfcuk-mail.test
    </p>
  </article>
</body>
</html>
```